Business card design needed

I need a business card for my new Food & Lifestyle Coaching business - "Bloomwell Food & Lifestlye Coaching"

i already have a logo and would like to have that incorporated into the business card, obviously.

i would like a design that says "fresh" and "funky" - my target market is female, aged 20-45 so i want something that will stand out to them when they see it.

My "Company Colour" is Apple Green
Updates

Thankyou to everyone who has submitted a design for my project. At this stage i have quite a large number of designs to chose from and with only a short time until my project closes i am focusing now on chosing from those i have already shortlisted so am unfortunately not considering any new desings.

Thankyou again for your interest in my project.

Target Market(s)

Female, Health Conscious (or looking to improve their health/lifestyle), aged between 20-45

Industry/Entity Type

Business

Contact Information for Business Card

Tessa Harlow
Ph: 0438215790
Email: hellobloom@quarlmail.com

Requirements
Must have
• Must include my existing Logo
Nice to have
• Would be nice to incoirporate and appointment card on the back

```html
<!DOCTYPE html>
<html lang="en">
<head>
<meta charset="utf-8">
<title>Bloomwell Food &amp; Lifestlye Coaching — Business Card</title>
<link rel="stylesheet" href="https://fonts.googleapis.com/css2?family=Arimo:wght@400;700&display=swap">
<style>
  :root {
    --page: #e6e6e4;
    --rose: #b95a62;
    --rose-light: #c46b72;
    --edge: #f7f5f2;
    --apple: #7ac943;
    --ink: #2b1f22;
    --white: #ffffff;
    --photo-a: #e9b9b9;
    --photo-b: #c9707a;
  }
  * { box-sizing: border-box; margin: 0; padding: 0; }
  html, body {
    width: 1200px; height: 1200px; overflow: hidden;
    background: var(--page);
    font-family: "Arimo", Arial, sans-serif;
  }
  .sheet {
    position: relative; width: 1200px; height: 1200px;
  }
  .card {
    position: absolute; left: 170px;
    width: 860px; height: 491px;
    background: var(--rose);
    border: 7px solid var(--edge);
    box-shadow: 0 6px 18px rgba(0,0,0,0.18);
    overflow: hidden;
  }
  .card--front { top: 80px; }
  .card--back  { top: 625px; }

  .brand {
    position: absolute; top: 36px; right: 40px;
    display: flex; align-items: center; gap: 14px;
    color: var(--ink);
  }
  .brand__dot {
    width: 46px; height: 46px; border-radius: 50%;
    background: var(--apple);
  }
  .brand__name {
    font-size: 50px; font-weight: 400; line-height: 1;
  }
  .brand__name small {
    display: block; font-size: 18px; margin-top: 6px; text-align: right;
  }

  .contact {
    position: absolute; left: 44px; top: 130px;
    color: var(--white); text-transform: uppercase;
  }
  .contact__name {
    font-size: 46px; font-weight: 700; letter-spacing: 1px;
    margin-bottom: 22px;
  }
  .contact__label {
    display: inline-block; font-size: 22px; font-weight: 700;
    border-bottom: 3px solid var(--apple); padding-bottom: 2px;
    margin-top: 12px;
  }
  .contact__value {
    font-size: 21px; font-weight: 400; margin-top: 4px;
  }
  .contact__note {
    font-size: 22px; font-weight: 700; margin-top: 16px; line-height: 1.1;
  }
  .contact__note span { display: block; font-weight: 400; font-size: 19px; }

  .hero-photo {
    position: absolute; right: 30px; bottom: 24px;
    width: 380px; height: 200px;
    border-radius: 6px;
    background: linear-gradient(120deg, var(--photo-a), var(--photo-b));
  }

  .appointment-lines {
    position: absolute; left: 60px; top: 150px;
    width: 740px; height: 300px;
  }
</style>
</head>
<body>
<main class="sheet">
  <section class="card card--front" aria-label="Business card front">
    <div class="brand">
      <span class="brand__dot"></span>
      <p class="brand__name">Bloomwell<small>Food &amp; Lifestlye Coaching</small></p>
    </div>
    <div class="contact">
      <h1 class="contact__name">Tessa Harlow</h1>
      <p class="contact__label">Phone</p>
      <p class="contact__value">043 821 5790</p>
      <p class="contact__label">E-mail</p>
      <p class="contact__value">hellobloom@quarlmail.com</p>
      <p class="contact__note">Scheduled<span>appointments on back</span></p>
    </div>
    <div class="hero-photo" role="img" aria-label="Photo of three smiling women enjoying fresh fruit"></div>
  </section>

  <section class="card card--back" aria-label="Appointment card back">
    <div class="brand">
      <span class="brand__dot"></span>
      <p class="brand__name">Bloomwell<small>Food &amp; Lifestlye Coaching</small></p>
    </div>
    <svg class="appointment-lines" viewBox="0 0 740 300" aria-hidden="true">
      <g stroke="#7ac943" stroke-width="3">
        <line x1="0" y1="20"  x2="740" y2="20"/>
        <line x1="0" y1="85"  x2="740" y2="85"/>
        <line x1="0" y1="150" x2="740" y2="150"/>
        <line x1="0" y1="215" x2="740" y2="215"/>
        <line x1="0" y1="280" x2="740" y2="280"/>
      </g>
    </svg>
  </section>
</main>
</body>
</html>
```